Invitation Design Project

I have my best friends Hens party and need to send out an email invitation.
The theme is 'Brunch by the Harbour' referring to the series with Norah lucinda barlow

details below:
4pm at 17 Marlow Crescent Dalkeith (Tessa's sisters house)
Bus to dinner at The Quarry Hotel in the city at for 7.30pm
Drinks in the city after dinner

Please RSVP to Maree Dunlop by Wednesday 6th of February maree.vance@coralnet.com.au

needs to say also that
Ssshhhhh please keep these details a secret from Tessa (or something along those lines)

Industry/Entity Type

Hotel

Requirements
Must have
• brunch by the harbour theme
Perth Western Australia is the location with characters from the brunch and the harbour series

```html
<!DOCTYPE html>
<html lang="en">
<head>
<meta charset="utf-8">
<title>Brunch by the Harbour – Hen's Invitation</title>
<link rel="stylesheet" href="https://fonts.googleapis.com/css2?family=Kaushan+Script&family=Federo&display=swap">
<style>
  :root {
    --ink: #120a10;
    --hot-pink: #e8197f;
    --soft-pink: #f6b9d6;
    --lilac: #d9a7e8;
    --teal: #3fd6c9;
    --glass-top: #8fb9bd;
    --white: #ffffff;
  }
  * { box-sizing: border-box; margin: 0; padding: 0; }
  html, body { width: 1000px; height: 1200px; overflow: hidden; }
  body { background: var(--white); }

  .invite {
    position: relative;
    width: 1000px;
    height: 1200px;
    overflow: hidden;
    background: linear-gradient(180deg,
      #fbe9f0 0%, #ffffff 8%, #fdf3e2 18%, #ffffff 30%,
      #fffbe6 70%, #fbf6d4 78%, #f3f7dc 84%, #f7e1f0 92%, #e7d6f4 100%);
  }

  .art { position: absolute; }
  .art--dancer {
    left: 60px; top: 0; width: 150px; height: 360px;
    border-radius: 40% 40% 30% 30%;
    background: linear-gradient(180deg, rgba(232,25,127,0.1), rgba(232,25,127,0.55) 50%, rgba(232,25,127,0.15));
  }
  .art--skyline {
    left: 0; top: 390px; width: 1000px; height: 470px;
    background: linear-gradient(180deg,
      rgba(255,255,255,0) 0%, rgba(240,190,210,0.5) 12%,
      rgba(120,100,80,0.4) 30%, rgba(200,160,60,0.45) 52%,
      rgba(255,255,255,0.7) 64%, rgba(63,214,201,0.45) 80%,
      rgba(255,255,255,0) 100%);
  }
  .art--cocktail {
    left: 770px; top: 240px; width: 230px; height: 900px;
  }

  .line { position: absolute; white-space: nowrap; color: var(--ink); }
  .script {
    font-family: "Kaushan Script", cursive;
    text-shadow: 0 0 3px var(--hot-pink), 0 0 6px var(--white), 2px 2px 0 var(--soft-pink);
  }
  .caps {
    font-family: "Federo", sans-serif;
    font-variant: small-caps;
    text-shadow: 0 0 4px var(--white), 0 0 8px var(--white), 1px 1px 0 var(--white);
  }

  .headline { left: 135px; top: 50px; font-size: 80px; transform: rotate(-9deg); transform-origin: left bottom; }
  .theme { left: 232px; top: 190px; font-size: 42px; }
  .guest { left: 235px; top: 262px; font-size: 78px; }
  .venue { left: 148px; top: 356px; font-size: 52px; transform: rotate(2deg); }
  .address { left: 215px; top: 462px; font-size: 36px; }
  .start-time { left: 355px; top: 510px; font-size: 54px; }
  .transport { left: 145px; top: 610px; font-size: 35px; }
  .transport--second { left: 360px; top: 662px; }
  .drinks { left: 145px; top: 720px; font-size: 32px; }
  .rsvp { left: 145px; top: 790px; font-size: 34px; }
  .rsvp--date { top: 846px; }
  .rsvp-email { left: 145px; top: 903px; font-size: 30px; letter-spacing: 1px; font-variant: normal; }
  .secret { left: 160px; top: 1080px; font-size: 46px; color: #2a0c2a; text-shadow: 0 0 4px var(--lilac), 2px 2px 0 var(--soft-pink); }

  .footer-bar { position: absolute; left: 60px; top: 1150px; width: 572px; height: 22px; background: var(--white); }
</style>
</head>
<body>
<main class="invite">
  <div class="art art--skyline" role="img" aria-label="Perth city skyline across the Swan River"></div>
  <div class="art art--dancer" role="img" aria-label="Woman in a flowing pink dress dancing"></div>
  <svg class="art art--cocktail" viewBox="0 0 230 900" role="img" aria-label="Pink cosmopolitan cocktail in a martini glass">
    <defs>
      <linearGradient id="cocktail-fill" x1="0" y1="0" x2="0" y2="1">
        <stop offset="0" stop-color="#8fb9bd"/>
        <stop offset="0.15" stop-color="#e8197f"/>
        <stop offset="0.4" stop-color="#e8197f" stop-opacity="0.7"/>
        <stop offset="1" stop-color="#d9a7e8" stop-opacity="0.8"/>
      </linearGradient>
    </defs>
    <rect x="0" y="0" width="230" height="900" fill="url(#cocktail-fill)" opacity="0.55"/>
  </svg>

  <h1 class="line script headline">Your Invited</h1>
  <p class="line caps theme">Brunch by the Harbour</p>
  <p class="line script guest">with Hen</p>
  <p class="line script venue">@Tessa's Sisters House</p>
  <p class="line caps address">17 Marlow Crescent Dalkeith</p>
  <p class="line script start-time">4pm</p>
  <p class="line caps transport">Bus to dinner at The Quarry Hotel</p>
  <p class="line caps transport transport--second">in the city at 7:30pm</p>
  <p class="line caps drinks">Drinks in the city after dinner</p>
  <p class="line caps rsvp">Please R.S.V.P. to Maree Dunlop by</p>
  <p class="line caps rsvp rsvp--date">Wednesday 6th of February</p>
  <p class="line caps rsvp-email">maree.vance@coralnet.com.au</p>
  <p class="line script secret">Ssshhhhh It's a Surprise</p>
  <div class="footer-bar"></div>
</main>
</body>
</html>
```